Door Company Flyer for October Hardware Sale

We are a door company and need a new flyer for a sale on hardware going on starting today thru the end of October (Oct 1st-Oct 31st) Our logo colors are gray, orange, and white. We need the 3 pictures of hardware included. Our company is TALVO Commercial Door, our supplier is Quorvane and the hardware on sale is Marten brand. We will need this in pdf format to print flyers and also a digital version to post on our website and social media.

```html
<!DOCTYPE html>
<html lang="en">
<head>
<meta charset="utf-8">
<title>TALVO Commercial Door – October Hardware Sale</title>
<link href="https://fonts.googleapis.com/css2?family=Poppins:ital,wght@0,400;0,600;0,700;1,400;1,600;1,700&display=swap" rel="stylesheet">
<style>
  :root{
    --orange:#f7962a;
    --orange-deep:#f28a1c;
    --gray-dark:#2c2c2c;
    --gray-logo:#8a8a8c;
    --gray-maker:#6e6f71;
    --gray-badge:#5f6062;
    --white:#ffffff;
    --yellow:#f6b324;
  }
  *{box-sizing:border-box;margin:0;padding:0}
  html,body{width:927px;height:1200px;overflow:hidden;background:var(--white)}
  body{font-family:"Poppins",sans-serif;color:var(--gray-dark)}
  .flyer{position:relative;width:927px;height:1200px;overflow:hidden;background:var(--white);border:1px solid #9a9a9a}

  .top-band{position:absolute;left:0;top:0;width:927px;height:112px;background:linear-gradient(180deg,#f2f2f3,#d9dadc)}
  .wall{position:absolute;left:0;top:110px;width:927px;height:520px;background:linear-gradient(135deg,#1f2c52 0%,#2f4173 45%,#3a4d85 100%)}
  .room-photo{position:absolute;left:357px;top:176px;width:570px;height:580px;background:linear-gradient(160deg,#f4f5f7 0%,#dfe2e7 45%,#b9c1cc 100%)}
  .white-cut{position:absolute;left:0;top:570px;width:927px;height:200px}
  .bottom-band{position:absolute;left:0;bottom:0;width:927px;height:29px;background:var(--orange)}

  .brand-tab{position:absolute;left:49px;top:0;width:319px;height:160px}
  .brand{position:absolute;left:49px;top:34px;width:319px;display:flex;align-items:center;justify-content:center;gap:10px}
  .brand-mark{width:30px;height:58px;background:var(--orange)}
  .brand-name{color:var(--gray-logo);font-weight:700;line-height:1}
  .brand-name .word{display:block;font-size:40px;letter-spacing:2px}
  .brand-name .sub{display:block;font-size:11.5px;letter-spacing:0.6px;margin-top:3px}

  .hardware-column{position:absolute;left:60px;top:112px;width:296px;height:880px;background:linear-gradient(135deg,var(--orange) 0%,var(--orange-deep) 100%);border-radius:0 0 34px 34px}

  .product-card{position:absolute;left:93px;width:230px;height:218px;background:var(--white);border-radius:16px;box-shadow:0 4px 10px rgba(0,0,0,.12);text-align:center;padding:61px 16px 0}
  .product-card h2{font-size:13px;font-weight:700;font-style:italic;color:#222;line-height:1.2;margin:0 -12px 2px;white-space:nowrap}
  .product-card p{font-size:8.4px;font-style:italic;line-height:10.5px;color:#333}
  .product-thumb{position:absolute;left:154px;width:108px;height:103px;background:var(--white);border:2px solid var(--orange);border-radius:8px;box-shadow:0 3px 6px rgba(0,0,0,.15);padding:8px;z-index:1}
  .product-thumb .shot{width:100%;height:100%;border-radius:4px;background:radial-gradient(circle at 50% 50%,#c9ccd1 0%,#eceef0 70%,#fff 100%)}

  .card-closer{top:264px}
  .thumb-closer{top:213px}
  .card-exit{top:553px}
  .thumb-exit{top:502px}
  .card-lever{top:843px}
  .thumb-lever{top:791px}

  .carrier-line{position:absolute;left:422px;top:815px;width:420px;text-align:center;font-size:23px;font-weight:600;font-style:italic;line-height:28px;color:var(--gray-dark)}
  .sale-line{position:absolute;left:422px;top:920px;width:420px;text-align:center;font-size:17px;font-weight:700;font-style:italic;line-height:22px;color:var(--orange-deep)}
  .sale-line span{display:block;font-size:14px;font-weight:600;color:var(--gray-dark)}

  .supplier-badge{position:absolute;left:522px;top:995px;width:86px;height:26px;background:var(--gray-badge);border-radius:6px;color:var(--white);font-size:15px;font-weight:700;font-style:italic;text-align:center;line-height:26px}
  .maker-name{position:absolute;left:505px;top:1038px;font-size:27px;font-weight:700;color:var(--gray-maker);line-height:34px}
  .partner-mark{position:absolute;left:673px;top:995px;width:49px;height:49px;background:var(--orange)}
  .partner-name{position:absolute;left:644px;top:1048px;font-size:17px;font-weight:600;color:#4a4a4c;letter-spacing:1px;line-height:22px}

  .contact{position:absolute;left:186px;top:1100px;width:420px;text-align:center;font-size:19px;font-style:italic;color:var(--gray-dark);line-height:25px}
  .contact-row{display:flex;align-items:center;justify-content:center;gap:6px}
  .contact-row svg{flex:none}

  .social{position:absolute;left:628px;top:1122px;display:flex;gap:10px}
  .social-item{display:flex;align-items:center;gap:4px;font-size:11px;font-weight:600;color:#3a3a3a}
  .social-dot{width:14px;height:14px;border-radius:50%;background:var(--yellow)}
</style>
</head>
<body>
<main class="flyer">
  <div class="top-band"></div>
  <div class="wall" role="img" aria-label="Dark blue textured wall photo"></div>
  <div class="room-photo" role="img" aria-label="Photo of glass folding doors opening onto a bright modern dining room"></div>
  <svg class="white-cut" viewBox="0 0 927 200" preserveAspectRatio="none" aria-hidden="true">
    <polygon points="0,12 360,180 927,6 927,200 0,200" fill="#ffffff"/>
  </svg>

  <div class="hardware-column"></div>

  <svg class="brand-tab" viewBox="0 0 319 160" aria-hidden="true">
    <path d="M0 0 H319 V116 Q240 128 175 150 Q160 158 145 150 Q80 128 0 116 Z" fill="#ffffff"/>
  </svg>
  <div class="brand">
    <div class="brand-mark"></div>
    <div class="brand-name"><span class="word">TALVO</span><span class="sub">COMMERCIAL DOOR</span></div>
  </div>

  <div class="product-thumb thumb-closer"><div class="shot" role="img" aria-label="Product photo of a surface mounted door closer"></div></div>
  <article class="product-card card-closer">
    <h2>Surface Mounted Door Closers</h2>
    <p>Commercial surface-mounted door closers are crucial tools for ensuring safe and controlled door operation in high-traffic locations. These surface-mounted closers provide dependable closing and latching mechanisms for the door. For closing large, regularly used doors, like those in office buildings, hotels, shops, and public spaces, they provide a practical and effective option. Surface-mounted door closers may often be customized to meet individual needs since they are able to handle a range of door weights and closing rates.</p>
  </article>

  <div class="product-thumb thumb-exit"><div class="shot" role="img" aria-label="Product photo of rim exit push bar devices"></div></div>
  <article class="product-card card-exit">
    <h2>Rim Exit Devices</h2>
    <p>Commercial rim exit devices are crucial safety and security elements for public and commercial buildings. These fixtures, which are commonly mounted on exit doors, offer a dependable way to leave quickly and easily in an emergency. A horizontal bar that covers the width of the door is a feature of rim escape devices. By pushing on the bar, individuals can quickly exit the building by unlatching the door. They are made of sturdy materials and designed to resist frequent use and possible misuse.</p>
  </article>

  <div class="product-thumb thumb-lever"><div class="shot" role="img" aria-label="Product photo of a commercial lever lock"></div></div>
  <article class="product-card card-lever">
    <h2>Lever Locks</h2>
    <p>Commercial door lever locks are strong, reliable locking devices created to improve the security and access management of establishments and public areas. These locks have an easy-to-use lever handle, making them user-friendly for both staff and clients. Stainless steel and brass are common components found in lever locks, ensuring their lifetime and resistance to tampering or forced entry attempts.</p>
  </article>

  <p class="carrier-line">As a Quorvane carrier, we carry<br>some of the best&nbsp; hardware on<br>the market including:</p>

  <p class="sale-line">Marten Hardware Sale<span>Oct 1st – Oct 31st</span></p>

  <div class="supplier-badge">Supplier</div>
  <div class="maker-name">MARTEN</div>
  <div class="partner-mark"></div>
  <div class="partner-name">QUORVANE</div>

  <address class="contact">
    <div class="contact-row">
      <svg width="15" height="15" viewBox="0 0 24 24" aria-hidden="true"><path d="M6.6 10.8a15.1 15.1 0 0 0 6.6 6.6l2.2-2.2a1 1 0 0 1 1-.25 11.4 11.4 0 0 0 3.6.57 1 1 0 0 1 1 1V20a1 1 0 0 1-1 1A17 17 0 0 1 3 4a1 1 0 0 1 1-1h3.5a1 1 0 0 1 1 1c0 1.25.2 2.45.57 3.6a1 1 0 0 1-.25 1z" fill="#2c2c2c"/></svg>
      <span>(555) 214-0398</span>
    </div>
    <div class="contact-row">
      <svg width="15" height="17" viewBox="0 0 24 24" aria-hidden="true"><path d="M12 2a7 7 0 0 0-7 7c0 5.25 7 13 7 13s7-7.75 7-13a7 7 0 0 0-7-7zm0 9.5A2.5 2.5 0 1 1 12 6.5a2.5 2.5 0 0 1 0 5z" fill="#2c2c2c"/></svg>
      <span>218 W Harlow St Ste B, Brookfield Tx.</span>
    </div>
  </address>

  <div class="social">
    <div class="social-item"><span class="social-dot"></span>Flockly</div>
    <div class="social-item"><span class="social-dot"></span>Pixgram</div>
  </div>

  <div class="bottom-band"></div>
</main>
</body>
</html>
```